Need a plumber

Would like a postcard sized flyer made up. Want the design to be kept very simple.
List of services we carry out in bullet point or similar.
Phone number and email included on the flyer.
Logo to feature prominantly.

List of services: Hot water issues
Burst Pipes
Gas Plumbing
Roof leaks
Drain blockages

Target Market(s)

Mums, dads and hosehgold owners

Industry/Entity Type

Plumbing

Colors
0054AA
0677BA
7BADD7
CADEEF
E8F1F8

Requirements
Must have
• Services we off and our logo, also must say "local plumber"

```html
<!DOCTYPE html>
<html lang="en">
<head>
<meta charset="utf-8">
<title>Need a Plumber – Clearflow Plumbing</title>
<link rel="stylesheet" href="https://fonts.googleapis.com/css2?family=Teko:wght@600&family=Montserrat:ital,wght@0,600;0,700;1,800&family=Oswald:wght@500&display=swap">
<style>
  :root {
    --page-bg: #e6e7e8;
    --navy: #0f56a8;
    --mid-blue: #0677ba;
    --ring-blue: #2c8fd2;
    --soft-blue: #7badd7;
    --white: #ffffff;
    --ink: #111111;
  }
  html, body {
    margin: 0;
    width: 875px;
    height: 1200px;
    overflow: hidden;
    background: var(--page-bg);
  }
  .flyer {
    position: absolute;
    left: 99px;
    top: 93px;
    width: 677px;
    height: 1014px;
    overflow: hidden;
    background: var(--mid-blue);
    font-family: "Montserrat", Arial, sans-serif;
  }
  .flyer-art {
    position: absolute;
    inset: 0;
    width: 677px;
    height: 1014px;
  }
  .headline {
    font-family: "Teko", "Arial Narrow", sans-serif;
    font-weight: 600;
  }
  .services {
    position: absolute;
    left: 28px;
    top: 468px;
    color: var(--white);
  }
  .services-title {
    margin: 0 0 10px;
    font-size: 34px;
    font-weight: 800;
    font-style: italic;
    letter-spacing: 0.5px;
  }
  .service-list {
    list-style: none;
    margin: 0;
    padding: 0;
  }
  .service-item {
    display: flex;
    align-items: center;
    height: 49px;
    font-size: 32px;
    font-weight: 600;
  }
  .service-icon {
    width: 25px;
    height: 25px;
    margin-right: 10px;
    flex: none;
  }
  .contact {
    position: absolute;
    left: 28px;
    top: 818px;
  }
  .contact-cta {
    margin: 0;
    font-size: 40px;
    font-weight: 700;
    color: var(--soft-blue);
    line-height: 1;
    letter-spacing: 0.5px;
  }
  .contact-phone {
    margin: 14px 0 0;
    font-family: "Oswald", "Arial Narrow", sans-serif;
    font-weight: 500;
    font-size: 72px;
    line-height: 1;
    color: var(--white);
  }
  .contact-email {
    margin: 18px 0 0;
    font-size: 21px;
    font-weight: 600;
    color: var(--soft-blue);
  }
  .brand-name {
    font-family: "Montserrat", Arial, sans-serif;
    font-weight: 700;
  }
</style>
</head>
<body>
  <main class="flyer">
    <svg class="flyer-art" viewBox="0 0 677 1014" xmlns="http://www.w3.org/2000/svg">
      <defs>
        <linearGradient id="bathroomTones" x1="0" y1="0" x2="1" y2="1">
          <stop offset="0" stop-color="#b9b4ac"/>
          <stop offset="0.5" stop-color="#d9d6d0"/>
          <stop offset="1" stop-color="#8f8a84"/>
        </linearGradient>
        <linearGradient id="repairTones" x1="0" y1="0" x2="1" y2="1">
          <stop offset="0" stop-color="#d8d8d8"/>
          <stop offset="0.6" stop-color="#a9a9ab"/>
          <stop offset="1" stop-color="#7a6f68"/>
        </linearGradient>
      </defs>

      <polygon class="band-headline" points="0,117 677,8 677,343 0,450" fill="var(--white)"/>
      <rect class="band-contact" x="0" y="778" width="677" height="236" fill="var(--navy)"/>

      <g class="headline">
        <text transform="translate(46 268) rotate(-9)" fill="var(--ink)" font-size="180" textLength="410" lengthAdjust="spacingAndGlyphs">NEED A</text>
        <text transform="translate(86 418) rotate(-9)" fill="var(--navy)" font-size="180" textLength="540" lengthAdjust="spacingAndGlyphs">PLUMBER</text>
      </g>

      <circle cx="557" cy="518" r="141" fill="var(--ring-blue)"/>
      <circle cx="557" cy="518" r="128" fill="url(#bathroomTones)" role="img" aria-label="Photo of a modern bathroom vanity with basins and mirror"/>
      <circle cx="585" cy="800" r="118" fill="var(--ring-blue)"/>
      <circle cx="585" cy="800" r="106" fill="url(#repairTones)" role="img" aria-label="Photo of a plumber repairing pipes under a sink"/>

      <circle cx="463" cy="729" r="87" fill="var(--white)"/>
      <circle cx="463" cy="729" r="83" fill="var(--ink)"/>
      <text class="brand-name" x="463" y="737" text-anchor="middle" font-size="22" fill="var(--white)" letter-spacing="2">CLEARFLOW</text>
    </svg>

    <section class="services">
      <h2 class="services-title">SERVICES</h2>
      <ul class="service-list">
        <li class="service-item"><svg class="service-icon" viewBox="0 0 24 24"><polygon points="12,1.5 21.5,7 21.5,17 12,22.5 2.5,17 2.5,7" fill="none" stroke="#fff" stroke-width="2.6"/><circle cx="12" cy="12" r="4.5" fill="none" stroke="#fff" stroke-width="2.6"/></svg>Hot Water Issues</li>
        <li class="service-item"><svg class="service-icon" viewBox="0 0 24 24"><polygon points="12,1.5 21.5,7 21.5,17 12,22.5 2.5,17 2.5,7" fill="none" stroke="#fff" stroke-width="2.6"/><circle cx="12" cy="12" r="4.5" fill="none" stroke="#fff" stroke-width="2.6"/></svg>Burst Pipes</li>
        <li class="service-item"><svg class="service-icon" viewBox="0 0 24 24"><polygon points="12,1.5 21.5,7 21.5,17 12,22.5 2.5,17 2.5,7" fill="none" stroke="#fff" stroke-width="2.6"/><circle cx="12" cy="12" r="4.5" fill="none" stroke="#fff" stroke-width="2.6"/></svg>Gas Plumbing</li>
        <li class="service-item"><svg class="service-icon" viewBox="0 0 24 24"><polygon points="12,1.5 21.5,7 21.5,17 12,22.5 2.5,17 2.5,7" fill="none" stroke="#fff" stroke-width="2.6"/><circle cx="12" cy="12" r="4.5" fill="none" stroke="#fff" stroke-width="2.6"/></svg>Roof Leaks</li>
        <li class="service-item"><svg class="service-icon" viewBox="0 0 24 24"><polygon points="12,1.5 21.5,7 21.5,17 12,22.5 2.5,17 2.5,7" fill="none" stroke="#fff" stroke-width="2.6"/><circle cx="12" cy="12" r="4.5" fill="none" stroke="#fff" stroke-width="2.6"/></svg>Drain Blockages</li>
      </ul>
    </section>

    <section class="contact">
      <p class="contact-cta">CALL NOW</p>
      <p class="contact-phone">0400 123 987</p>
      <p class="contact-email">info@clearflowplumbing.com.au</p>
    </section>
  </main>
</body>
</html>
```